Resume redesign

I'm a researcher who works with web design companies. I'm updating my resume but want more than the standard black and white wall of text. The content is updated, what I need is a design to make it readable, or in the words of my friend the hiring manager 'it needs to have high scan value'. It has to strike some balance between professionalism and readability.

There are two versions of my resume attached. I'm willing to cut some information if needed or reword things to simplify them. It would be great if it could be cut down to 2 pages, although this may require eliminating the publications section (which is fine).

```html
<!DOCTYPE html>
<html lang="en">
<head>
<meta charset="utf-8">
<title>Daniel Reyes – Resume</title>
<link href="https://fonts.googleapis.com/css2?family=Arimo:ital,wght@0,400;0,700;1,400&family=Archivo+Narrow:wght@400;600&family=Libre+Franklin:wght@700;800&display=swap" rel="stylesheet">
<style>
:root{
  --backdrop:#5a3420;
  --paper:#ffffff;
  --ink:#1e1e1e;
  --muted:#3c3c3c;
  --ribbon:#8a8a8a;
  --rule:#555555;
}
*{box-sizing:border-box;margin:0;padding:0}
html,body{width:1200px;height:741px;overflow:hidden}
body{background:var(--backdrop);position:relative;font-family:"Arimo",Arial,sans-serif;color:var(--ink)}
.page{position:absolute;background:var(--paper);overflow:hidden;padding:0 24px;font-size:6.8px;line-height:1.4;box-shadow:0 4px 14px rgba(0,0,0,.45)}
.page--one{left:122px;top:46px;width:456px;height:648px}
.page--two{left:630px;top:64px;width:456px;height:628px;padding-top:8px}
.ribbon{display:block;margin:10px auto 4px;width:200px;height:40px}
.contact{display:flex;gap:18px;font-size:6.8px;margin:0 10px 3px;border-bottom:.6px solid var(--rule);padding-bottom:2px}
.contact span:last-child{margin-left:auto}
.summary{margin:4px 0 4px}
.skills-title{text-align:center;font-size:6.4px;margin:4px 0}
.skills{text-align:center;font-size:6.2px;padding:0 6px;line-height:1.5}
.section-head{display:flex;align-items:center;gap:4px;margin:7px -8px 5px;font-family:"Libre Franklin",Arial,sans-serif;font-weight:800;font-size:8.4px;letter-spacing:.5px}
.section-head::before,.section-head::after{content:"";flex:1;height:.8px;background:var(--rule)}
.section-head .diamond{width:5px;height:5px;background:var(--rule);transform:rotate(45deg)}
.employer{display:flex;align-items:baseline;border-bottom:.8px solid var(--rule);font-family:"Archivo Narrow",Arial,sans-serif;font-size:9.8px;margin:6px -6px 3px;padding:0 0 1px}
.employer .place{font-size:6px;margin-left:6px}
.employer .place--city{font-size:7.2px}
.employer .years{margin-left:auto;font-size:9.6px}
.employer .years--small{font-size:7.8px}
.employer .years small{font-size:6px}
.tagline{font-style:italic;margin-bottom:4px}
.role{font-family:"Libre Franklin",Arial,sans-serif;font-weight:700;font-size:7px;margin:5px 0 2px}
.role .dates{font-weight:400}
.role--light{font-family:"Archivo Narrow",Arial,sans-serif;font-weight:400;font-size:7.6px;letter-spacing:.3px}
.project{font-family:"Libre Franklin",Arial,sans-serif;font-weight:700;font-size:6.8px;margin-top:3px}
.methods,.label{font-style:italic;margin:2px 0 3px}
.bullets{list-style:none;padding-left:30px}
.bullets li::before{content:"- "}
.education{text-align:center;font-family:"Libre Franklin",Arial,sans-serif;font-weight:700;font-size:6.8px;line-height:1.55}
.education .note{font-family:"Arimo",Arial,sans-serif;font-weight:400}
</style>
</head>
<body>

<article class="page page--one">
  <svg class="ribbon" viewBox="0 0 200 40" role="img" aria-label="Daniel Reyes, PhD, MBA – Research Consultant">
    <polygon points="0,4 200,4 188,20 200,36 0,36 12,20" fill="#8a8a8a"/>
    <text x="100" y="18" text-anchor="middle" font-family="Archivo Narrow, Arial, sans-serif" font-size="11" fill="#fff">DANIEL REYES, PHD, MBA</text>
    <text x="100" y="30" text-anchor="middle" font-family="Archivo Narrow, Arial, sans-serif" font-size="6.5" fill="#fff" letter-spacing=".6">RESEARCH CONSULTANT</text>
  </svg>
  <p class="contact"><span>daniel@tallpineresearch.com</span><span>(555) 014-2290</span><span>14 Alder Court, Brookfield, OR 97001</span></p>
  <p class="summary">Forward-thinking and dynamic Senior Research Consultant with experience leading targeted research strategies and data collection initiatives to drive project success and reduce spending. Expert communicator who leverages strong research acumen to obtain key customer insight, collect and analyze data, and provide accurate primary and secondary findings to deliver value-enhancing recommendations across major, multimillion dollar projects with organizations including Meridian Telecom, Hollis Pharmacy, Corvex, and Northway Bank. Expertise in developing customized and detailed research solutions to fit the scope of a range of projects and ensure accurate and profitable results.</p>
  <p class="skills-title">Areas of expertise:</p>
  <p class="skills">RESEARCH DESIGN – QUANTITATIVE &amp; QUALITATIVE DATA COLLECTION – PRIMARY &amp; SECONDARY RESEARCH – STATISTICAL ANALYSIS – ETHNOGRAPHY – MATRIX ANALYSIS – STRUCTURED CULTURAL DOMAIN ANALYSIS – TEXT ANALYSIS – SOCIAL MEDIA ANALYSIS – MULTIVARIATE ANALYSIS – STRATEGIC PLANNING – NON-PARAMETRIC &amp; CATEGORICAL ANALYSIS – ONLINE &amp; ON-SITE INTERVIEWS – PANEL MANAGEMENT – USABILITY TESTING – OBSERVATIONAL TESTING – SURVEY MANAGEMENT – FOCUS GROUPS – COGNITIVE ANTHROPOLOGY – IDIOGRAPHIC RESEARCH – STATCORE – DATAPRO – CB</p>

  <h2 class="section-head"><span class="diamond"></span>PROFESSIONAL EXPERIENCE<span class="diamond"></span></h2>

  <div class="employer">TALL PINE RESEARCH, LLC. –<span class="place">BROOKFIELD, OR</span><span class="years">2007 <small>TO</small> PRESENT</span></div>
  <p class="tagline">Boutique research firm providing customized solutions around consumer behavior, segmentation, and cultural models.</p>
  <h3 class="role">PRINCIPLE RESEARCHER</h3>
  <p>Design and implement effective, top-tier research design for a range of projects and industries. Directly interface with clients to communicate research processes and findings while collecting and analyzing appropriate types of data to recommend easily understood, actionable, and highly customized solutions and results.</p>
  <p class="label">Selected Projects:</p>
  <p class="project">Journal of Applied Science Teaching</p>
  <p>Project to understand readership segmentation and the utilization of both print and online versions of the publication. Implemented online survey to collect data from 1.6K+ respondents.</p>
  <p class="methods">Methods: Survey design, sampling, web survey programming, quantitative data analysis, multivariate analysis.</p>
  <p class="project">Norvale Electronics</p>
  <p>Designed and moderated usability testing in pre-launch development test for a new television at Norvale Electronics. Analyzed recordings for patterns of its use among participants and why issues were significant to users. Suggested solutions to alleviate all problems.</p>
  <p class="methods">Methods: Usability test moderation, transcript analysis.</p>
  <p class="project">Regional Utility Company</p>
  <p>Developed research project in coordination with CRU to examine apartment owner infrastructure upgrades to reduce the use of utilities. Moderated two focus groups and directly presented findings to CRU.</p>
  <p class="methods">Methods: Focus group moderation, text analysis.</p>

  <div class="employer">BLUEFIN INTERACTIVE –<span class="place place--city">Lakeport, MI</span><span class="years">2008 <small>TO</small> 2013</span></div>
  <p class="tagline">Leading global interactive agency providing services including web development, media planning, and creative marketing.</p>
  <h3 class="role role--light">CONTRACTED SENIOR RESEARCHER</h3>
  <p>Drove and developed key primary and secondary research to create practical findings and compose detailed research plans for a range of multimillion dollar digital projects. Collected and analyzed data for both internal and external clients. Collaborated with customers to understand and implement findings within their organizations. Heavily researched industry trends and provided competitive analysis. Managed research vendors to ensure projects were completed on time and within budget.</p>
  <p class="label">Selected Projects:</p>
  <p class="project">Threshold</p>
  <p>Collected and analyzed data provided by Datawell and Skyline Air to better understand how consumers define engagement and how various platforms create engaging brand experiences. thresholdstudy.example</p>
  <p class="methods">Methods: Phone interviews, online card sort, online survey, descriptive and multivariate statistical analysis.</p>
</article>

<article class="page page--two">
  <p class="contact"><span>daniel@tallpineresearch.com</span><span>(555) 014-2290</span><span>14 Alder Court, Brookfield, OR 97001</span></p>
  <p class="project">Hollis Pharmacy Customer Experience Benchmarking</p>
  <p>Major research initiative to guide the improvement of existing Hollis Pharmacy site as well as to inform future projects both on and offline. Conducted home interviews with respondents throughout the greater Lakeport area to understand Pharmaceutical Benefit Management consumer experience.</p>
  <p class="methods">Methods: In-home interviews, text analysis.</p>
  <p class="project">Meridian Telecom Business Services Web Taxonomy</p>
  <p>Developed two large online pile sorts to understand the mental categories used by respondents and restructure Meridian Telecom's B2B website taxonomy. Created an open sort gauging general categories in which B2B technology customers grouped services and a closed sort to confirm revised website taxonomy. Instituted short online survey during recruiting process.</p>
  <p class="methods">Methods: Card sorts, metric analysis, statistical analysis.</p>
  <p class="project">Personified Segmentation for Major Insurance Company</p>
  <p>Designed interview instrument used for both agent and consumer interviews conducted throughout three major metropolitan cities. Conducted 90-minute home interviews in four major cities on insurance usage and household financial management systems. Analyzed notes and recordings for major components used in large national survey to produce personified segments of U.S. insurance clients.</p>
  <p class="methods">Methods: Ethnographic interviews, text analysis.</p>
  <p class="project">Corvex Premier</p>
  <p>Constructed online card sorting tool, reducing respondent bias and resolving stakeholder concerns while analyzing data to determine navigational functionality of the Corvex Premier website. Transformed data into statistically manageable data body.</p>
  <p class="methods">Methods: Card sorts, matrix analysis.</p>
  <p class="project">Meridian Telecom Help and Support</p>
  <p>Transformed user insights to unique and innovative solutions to online help and support systems. Integral in the development and execution of focus groups in Lakeport and Bayview to realize desired set of features for Meridian's customer support. Modeled core features of principle drivers of help and support based on user observations and other ethnographic data.</p>
  <p class="methods">Methods: Focus Groups, text analysis</p>

  <div class="employer">UNIVERSITY OF ASHFORD SURVEY RESEARCH CENTER –<span class="place">BROOKFIELD, OR</span><span class="years years--small">2003 <small>TO</small> 2007</span></div>
  <p class="tagline">Conducts an assortment of surveys commissioned largely by state agencies and is one of the largest university survey programs in the country.</p>
  <h3 class="role">FIELD DIRECTOR <span class="dates">(2007)</span></h3>
  <p>Oversaw the hiring, training, scheduling, and general management of 200+ phone interviewers. Managed small teams of employees responsible for the construction of research designs emphasizing validity, accuracy, and precision.</p>
  <ul class="bullets">
    <li>Project scopes ranged from small surveys for private business to surveys with 10K+ completes for government agencies and offices.</li>
    <li>Increased productivity by developing and implementing innovative data-based evaluation system.</li>
  </ul>
  <h3 class="role">PROGRAM MANAGER/GRADUATE RESEARCH ASSISTANT <span class="dates">(2001 to 2006)</span></h3>
  <p>Directed full survey project lifecycle for research center under the Office of Regional Economic Studies. Spearheaded all efforts regarding telephone survey questionnaire development, CB programming, sample management, data cleaning, and analysis and report production.</p>
  <ul class="bullets"><li>Used StatCore to track lab productivity and complete large dataset analysis.</li></ul>
  <h3 class="role">ETHNOGRAPHER, SOCIAL NETWORK PROJECTS <span class="dates">(2004)</span></h3>
  <p>Collected egocentric network data on Mexican migrants in Northwestern Kansas in relation to Civic Science Fund grant under Dr. Ellen Marsh. Formulated models of acculturation and enculturation based on ethnographic field work and network data.</p>
  <p class="label">Selected Project:</p>
  <p class="project">Regional Parks and Forests Service</p>
  <p>Created discussion guide and moderated and analyzed two focus groups on the usage of Regional Forest Explorer annual passes. Screened focus group participants.</p>

  <h2 class="section-head"><span class="diamond"></span>EDUCATION &amp; CERTIFICATIONS<span class="diamond"></span></h2>
  <div class="education">
    <p>Ph.D. in Anthropology, Research Methodology – University of Ashford</p>
    <p>Master of Business Administration – Harlan State University</p>
    <p>Bachelor of Arts in Anthropology – Prairie State University</p>
    <p class="note">Civic Science Fund Summer Institute for Research Design in Cultural Anthropology</p>
  </div>
</article>

</body>
</html>
```